Tollo Pollution Mask Packaging

We need a packaging design for a pollution mask, image of mask attached. Have also attached a file with the exact measurements of the box.
There is also an example of a box attached, we would like a similar type design.
I have also attached the Logo, which should be fairly prominent in design.
The following blurb also needed:
Activated carbon dust mask.
99.999% Filtration
Instructions:
1: Place mask over mouth and nose.
2: Ensure aluminium bridge on top.
3: Adjust Gripzo on back to desired tension.
4: Additional Filters sold separately.
Material Description
1: Filter 10% Ammonia
2: N99 Filter Cotton
3: CR Material 100% Neoprene
4: N Cloth 100% Nylon
- RR Beaver

```html
<!DOCTYPE html>
<html lang="en">
<head>
<meta charset="utf-8">
<title>Tollo Pollution Mask Packaging</title>
<link href="https://fonts.googleapis.com/css2?family=Source+Sans+3:wght@400&display=swap" rel="stylesheet">
<style>
  :root {
    --leaf-green: #86c443;
    --ink-black: #000000;
    --paper-white: #ffffff;
    --mask-tone: #f3f3f3;
    --fold-grey: #3a3a3a;
    --text-font: "Source Sans 3", "Myriad Pro", Arial, sans-serif;
  }
  html, body {
    margin: 0;
    padding: 0;
    width: 1200px;
    height: 1200px;
    overflow: hidden;
    background: var(--paper-white);
  }
  .dieline {
    display: block;
    width: 1200px;
    height: 1200px;
    font-family: var(--text-font);
  }
  .flap { fill: var(--leaf-green); }
  .fold-line { stroke: var(--ink-black); stroke-width: 2.5; fill: none; }
  .side-fold { stroke: var(--fold-grey); stroke-width: 2; fill: none; }
  .panel-dark { fill: var(--ink-black); }
  .panel-front { fill: var(--paper-white); stroke: var(--ink-black); stroke-width: 2; }
  .hang-hole { fill: var(--paper-white); stroke: var(--ink-black); stroke-width: 1; }
  .copy-light { fill: var(--paper-white); font-size: 20px; }
  .copy-dark { fill: var(--ink-black); font-size: 16.5px; }
  .barcode-area { fill: var(--paper-white); }
  .barcode-label { fill: var(--ink-black); font-size: 11px; }
  .brand-name { fill: var(--leaf-green); font-size: 96px; letter-spacing: 10px; }
  .brand-dot { fill: var(--leaf-green); }
  .mask-visual { fill: var(--mask-tone); }
</style>
</head>
<body>
<svg class="dieline" viewBox="0 0 1500 1500" xmlns="http://www.w3.org/2000/svg">

  <!-- Glue flap -->
  <path class="flap" d="M198 188 H285 L298 270 L305 745 L290 832 H205 L200 750 L193 742 V280 L198 270 Z"/>

  <!-- Back top closure -->
  <g class="back-top">
    <path class="flap" d="M315 22 H700 L710 45 L712 160 H303 L303 50 Z"/>
    <rect class="flap" x="303" y="160" width="410" height="114"/>
    <line class="fold-line" x1="303" y1="160" x2="712" y2="160"/>
    <path class="hang-hole" d="M467 120 H546 A7 7 0 0 1 546 134 H518 Q506 146 494 134 H467 A7 7 0 0 1 467 120 Z"/>
    <path class="hang-hole" d="M467 190 H494 Q506 178 518 190 H546 A7 7 0 0 1 546 204 H467 A7 7 0 0 1 467 190 Z"/>
  </g>

  <!-- Back panel -->
  <g class="back-panel">
    <rect class="panel-dark" x="300" y="272" width="417" height="472"/>
    <path class="flap" d="M480 705 H544 V760 Q544 782 520 782 H500 Q480 782 480 760 Z"/>
    <text class="copy-light" x="319" y="329">
      <tspan x="319">Instructions:</tspan>
      <tspan x="319" dy="24">1: Place mask over mouth and nose.</tspan>
      <tspan x="319" dy="24">2: Ensure aluminium bridge on top.</tspan>
      <tspan x="319" dy="24">3: Adjust Gripzo on back to desired tension.</tspan>
      <tspan x="319" dy="24">4: Additional Filters sold separately.</tspan>
      <tspan x="319" dy="48">Material Description</tspan>
      <tspan x="319" dy="24">1: Filter 10% Ammonia</tspan>
      <tspan x="319" dy="24">2: N99 Filter Cotton</tspan>
      <tspan x="319" dy="24">3: CR Material 100% Neoprene</tspan>
      <tspan x="319" dy="24">4: N Cloth 100% Nylon</tspan>
    </text>
  </g>

  <!-- Side panel -->
  <g class="side-panel">
    <path class="panel-dark" d="M733 184 H819 Q821 186 821 190 L822 272 H719 L720 255 Q722 250 725 240 Z"/>
    <rect class="panel-dark" x="719" y="272" width="107" height="473"/>
    <path class="panel-dark" d="M720 745 H824 L823 828 Q820 832 815 832 H734 L727 770 Q721 760 720 750 Z"/>
    <line class="side-fold" x1="718" y1="272" x2="718" y2="745"/>
    <rect class="barcode-area" x="730" y="670" width="85" height="43"/>
    <text class="barcode-label" x="741" y="694">BARCODE</text>
  </g>

  <!-- Front top closure -->
  <g class="front-top">
    <path class="flap" d="M855 118 H1215 Q1240 118 1240 145 V162 H833 V140 Q833 118 855 118 Z"/>
    <rect class="flap" x="830" y="162" width="413" height="113"/>
    <line class="fold-line" x1="833" y1="162" x2="1241" y2="162"/>
  </g>

  <!-- Front panel -->
  <g class="front-panel">
    <rect class="panel-front" x="826" y="275" width="416" height="470"/>
    <circle class="brand-dot" cx="892" cy="342" r="44"/>
    <text class="brand-name" x="962" y="360">Tollo</text>
    <rect class="mask-visual" role="img" aria-label="Line illustration of the activated carbon dust mask"
          x="938" y="420" width="254" height="240" rx="10"/>
    <text class="copy-dark" x="846" y="673">Activated carbon dust mask.</text>
    <text class="copy-dark" x="846" y="712">99.999% Filtration</text>
  </g>

  <!-- Right dust flap -->
  <path class="flap" d="M1242 275 L1283 285 V733 L1242 743 Z"/>

  <!-- Front bottom closure -->
  <g class="front-bottom">
    <rect class="flap" x="828" y="745" width="415" height="110"/>
    <path class="flap" d="M832 855 H1240 V875 Q1240 900 1215 900 H857 Q832 900 832 875 Z"/>
    <line class="fold-line" x1="832" y1="855" x2="1241" y2="855"/>
  </g>
</svg>
</body>
</html>
```